Business Cards for Branding (Advertising) Agency

We need stylish and cool business cards.
Additional info:
1) Logo - see the attachment. You can use either the three penguins or just one penguin face (square or round) - at your discretion.
2) Text and other stuff for business card:
front side:
-Logo and company name: company name - Northern Herons - should be in English as is in logo. This is the only exception. The rest of the text will be in Russian.
-Who we are: Брендинговое агентство
-First and last name:
-Position: Управляющий партнёр
-Address:
-Phone:
-Email:
-Website:
Note: please don't use names of information fields, such as: who we are, first and last name, position, address, phone, email and website.

3) Our suggestions on design:
-The backside of the business card can be either blank or has something on it - at your discretion.
-The business card background should be either white or grey (you can use any tone of grey).

Additional Information:
1) БРЕНДИНГОВОЕ АГЕНТСТВО
2) ул. Верескова - these two words should be together on the same line
3) тел.: +7 (495) 381-60-92
моб.: +7 (916) 507-28-14

Reason: We would like to receive more stylish designs.

```html
<!DOCTYPE html>
<html lang="ru">
<head>
<meta charset="utf-8">
<title>Northern Herons — визитные карточки</title>
<link rel="stylesheet" href="https://fonts.googleapis.com/css2?family=PT+Sans:wght@400;700&display=swap">
<style>
  :root {
    --backdrop: #ecebe6;
    --card: #ffffff;
    --card-edge: #d6d6d6;
    --band: #dcdde1;
    --band-light: #ebecef;
    --band-mid: #c9cbd0;
    --ink: #2b2b2b;
    --mark: #1e1e1e;
  }
  * { box-sizing: border-box; margin: 0; padding: 0; }
  html, body {
    width: 1200px; height: 705px; overflow: hidden;
    background: var(--backdrop);
    font-family: "PT Sans", Arial, sans-serif;
    color: var(--ink);
  }
  .stage { position: relative; width: 1200px; height: 705px; }

  .card {
    position: absolute;
    background: var(--card);
    border: 1px solid var(--card-edge);
    overflow: hidden;
  }

  /* Front, vertical */
  .card--front { left: 152px; top: 116px; width: 335px; height: 530px; }
  .card--front .bands { position: absolute; left: 0; top: 0; width: 335px; height: 530px; }
  .brand {
    position: absolute; left: 0; right: 0;
    display: flex; align-items: center; justify-content: center; gap: 10px;
    color: var(--mark);
  }
  .brand__dot { width: 22px; height: 22px; border-radius: 50%; background: var(--mark); }
  .brand__name { font-weight: 700; letter-spacing: 0.04em; }
  .card--front .brand { top: 82px; }
  .card--front .brand__name { font-size: 22px; }

  .details {
    position: absolute; left: 61px; top: 196px;
    font-size: 17px; line-height: 22px;
  }
  .details__tagline { margin-bottom: 22px; }
  .details__person { text-decoration: underline; }
  .details__role { font-weight: 700; }
  .details__address { margin-top: 22px; }
  .details__site { margin-top: 22px; }

  /* Back, horizontal */
  .card--back { left: 548px; top: 173px; width: 573px; height: 335px; }
  .card--back .brand { top: 145px; gap: 14px; }
  .card--back .brand__dot { width: 34px; height: 34px; }
  .card--back .brand__name { font-size: 34px; }
</style>
</head>
<body>
<main class="stage">

  <section class="card card--front" aria-label="Лицевая сторона визитки">
    <svg class="bands" viewBox="0 0 335 530" aria-hidden="true">
      <polygon points="0,150 167,182 335,150 335,190 0,190" fill="var(--band-mid)"/>
      <polygon points="0,118 167,168 335,118 335,150 167,182 0,150" fill="var(--band-light)"/>
      <rect x="0" y="190" width="335" height="340" fill="var(--band)"/>
    </svg>

    <div class="brand">
      <span class="brand__dot"></span>
      <span class="brand__name">Northern Herons</span>
    </div>

    <div class="details">
      <p class="details__tagline">Брендинговое агентство</p>
      <p class="details__person">Мария Соколова</p>
      <p class="details__role">Управляющий партнёр</p>
      <p class="details__phone">+7 (916) 507-28-14</p>
      <p class="details__email">maria@northernherons.ru</p>
      <p class="details__address">117312, г. Москва, ул.<br>Верескова, д.12, стр.2</p>
      <p class="details__site">www.northernherons.ru</p>
    </div>
  </section>

  <section class="card card--back" aria-label="Оборотная сторона визитки">
    <div class="brand">
      <span class="brand__dot"></span>
      <span class="brand__name">Northern Herons</span>
    </div>
  </section>

</main>
</body>
</html>
```